FLyer

We need A4 tri-fold flyers which matches the colours of existing company logo.
We are a physiotherapy clinic wanting to promote
1. who we are
2. what we treat (conditions or injuries)
3. how we treat ( manual therapy, manipulation, acupuncture, exercise, Ultrasound/laser etc)

Industry/Entity Type

Clinic

```html
<!DOCTYPE html>
<html lang="en">
<head>
<meta charset="utf-8">
<title>Peak Stride Physiotherapy – Tri-fold Flyer</title>
<link rel="stylesheet" href="https://fonts.googleapis.com/css2?family=PT+Sans:wght@400;700&family=Kaushan+Script&display=swap">
<style>
:root{
  --backdrop:#6b6b6b;
  --paper:#ffffff;
  --green:#3cb54a;
  --green-deep:#2ea844;
  --lime:#c3d94a;
  --lime-soft:#d6e46a;
  --text:#6a6a6a;
  --heading-green:#4cb848;
  --photo-skin:#d9b49a;
  --photo-sky:#c9d6dc;
  --photo-field:#8fa25e;
  --photo-people:#c9bfb8;
}
*{margin:0;padding:0;box-sizing:border-box}
html,body{width:1200px;height:489px;overflow:hidden;background:var(--backdrop)}
body{position:relative;font-family:"PT Sans",Arial,sans-serif;color:var(--text)}
.sheet{position:absolute;background:var(--paper);overflow:hidden}
.sheet--outside{left:15px;top:8px;width:582px;height:450px}
.sheet--inside{left:614px;top:8px;width:574px;height:450px}
.abs{position:absolute}
.blob{position:absolute}
.panel-title{position:absolute;color:#fff;font-size:12.5px;letter-spacing:.2px;text-transform:uppercase}
.body-copy{position:absolute;font-size:7.6px;line-height:10.6px;color:var(--text)}
.body-copy p+p{margin-top:10px}
.photo{position:absolute}
.brand{position:absolute;display:flex;align-items:center;gap:6px}
.brand__dot{width:30px;height:30px;border-radius:50%;background:var(--green)}
.brand__name{font-size:22px;font-weight:700;color:var(--green);line-height:1}
.brand__tag{font-size:8px;font-weight:700;color:var(--green);letter-spacing:.2px;margin-top:2px}
.contact{position:absolute;left:225px;top:263px;width:165px;text-align:center;color:#fff;font-size:8.2px;line-height:11px}
.contact .gap{height:16px}
.tagline{position:absolute;font-family:"Kaushan Script",cursive;color:#fff;font-size:13px}
.service{position:absolute;width:168px}
.service h3{font-size:8.2px;font-weight:400;color:var(--heading-green);text-transform:uppercase;margin-bottom:5px;letter-spacing:.1px}
.service p{font-size:7.4px;line-height:10.2px;color:var(--text)}
</style>
</head>
<body>

<section class="sheet sheet--outside">
  <svg class="blob" style="left:0;top:0" width="160" height="125" viewBox="0 0 160 125">
    <path d="M0 0H138C156 25 150 70 118 95C88 118 40 122 0 112Z" fill="var(--lime)"/>
    <path d="M0 0H128C142 28 132 68 104 88C78 106 38 110 0 102Z" fill="var(--green)"/>
  </svg>
  <h2 class="panel-title" style="left:20px;top:36px">Who we are?</h2>

  <div class="body-copy" style="left:18px;top:129px;width:167px">
    <p>At Peak Stride Physiotherapy, we don't just treat the injury, we treat the whole person. Each of our clients receives a comprehensive evaluation and examination in a private one-on-one treatment room.</p>
    <p>We offer extended appointment times to ensure that all of your concerns are recognized and incorporated into an individualized treatment plan that works for you and your lifestyle. We pride ourselves on working closely with your team of health care professionals, coaches and trainers to ensure the best management of your needs.</p>
  </div>

  <div class="photo" role="img" aria-label="Photo of a physiotherapist stretching a patient's arm" style="left:0;top:290px;width:190px;height:160px;background:linear-gradient(120deg,var(--photo-people),#e9e4e0 45%,#9a86b8)"></div>

  <div class="brand" style="left:208px;top:104px">
    <span class="brand__dot"></span>
    <div><div class="brand__name">peakstride</div><div class="brand__tag">PHYSIOTHERAPY &amp; SPORTS CLINIC</div></div>
  </div>
  <div class="brand" style="left:402px;top:20px">
    <span class="brand__dot"></span>
    <div><div class="brand__name">peakstride</div><div class="brand__tag">PHYSIOTHERAPY &amp; SPORTS CLINIC</div></div>
  </div>

  <div class="photo" role="img" aria-label="Photo of a woman cycling on a country path" style="left:387px;top:75px;width:195px;height:220px;background:linear-gradient(180deg,var(--photo-sky),#b7c4b6 45%,var(--photo-field))"></div>

  <svg class="blob" style="left:190px;top:180px" width="392" height="270" viewBox="0 0 392 270">
    <path d="M40 40C110 5 250 -5 340 25C385 40 400 90 380 150C360 210 300 262 200 266C110 270 30 240 8 170C-8 110 5 60 40 40Z" fill="var(--lime)"/>
    <path d="M30 40C100 0 230 0 300 30C345 50 350 110 320 160C290 210 230 245 150 250C80 254 20 225 6 165C-4 115 5 60 30 40Z" fill="var(--green)" opacity=".92"/>
  </svg>

  <address class="contact" style="font-style:normal">
    Shop 4, The Arcade 212 Harbour Rd,<br>Linwood 2071
    <div class="gap"></div>
    Phone: (02) 5550 1234<br>Fax: (02) 5550 5678<br>info@peakstridephysio.com.au<br>www.peakstridephysio.com
  </address>
  <p class="tagline" style="left:400px;top:260px">Attention you Deserve</p>
  <p class="tagline" style="left:440px;top:286px">Result you Desire</p>
</section>

<section class="sheet sheet--inside">
  <div class="photo" role="img" aria-label="Photo of hands massaging a shoulder" style="left:0;top:6px;width:188px;height:205px;background:linear-gradient(135deg,#f1e4dc,var(--photo-skin) 55%,#c89a80)"></div>
  <svg class="blob" style="left:0;top:90px" width="170" height="125" viewBox="0 0 170 125">
    <path d="M0 25C40 0 130 2 158 40C172 62 165 100 140 117H0Z" fill="var(--lime)"/>
    <path d="M0 30C40 8 120 10 145 45C158 65 150 100 128 117H0Z" fill="var(--green)"/>
  </svg>
  <h2 class="panel-title" style="left:22px;top:141px">What we do?</h2>

  <div class="body-copy" style="left:10px;top:244px;width:172px">
    <p>Lorem ipsum dolor sit amet, consectetuer adipiscing elit, sed diam nonummy nibh euismod tincidunt ut laoreet dolore magna aliquam erat volutpat. Ut wisi enim ad minim veniam, quis nostrud exerci tation ullamcorper suscipit lobortis nisl ut aliquip ex ea commodo consequat. Duis autem vel eum iriure dolor in hendrerit in vulputate velit esse molestie consequat, vel illum dolore eu feugiat nulla facilisis at vero eros et accumsan et iusto odio dignissim qui blandit praesent luptatum zzril delenit augue duis dolore te feugait nulla facilisi.</p>
    <p>Nam liber tempor cum soluta nobis eleifend option congue nihil imperdiet doming id quod mazim placerat facer possim assum. Typi non habent claritatem insitam; m clari, fiant sollemnes in futurum.</p>
  </div>

  <svg class="blob" style="left:194px;top:0" width="190" height="92" viewBox="0 0 190 92">
    <path d="M8 0H186C192 35 175 75 130 86C80 96 25 80 10 50C2 32 2 12 8 0Z" fill="var(--lime)"/>
    <path d="M14 0H176C180 30 165 66 125 76C82 85 35 72 20 45C12 30 10 12 14 0Z" fill="var(--green)"/>
  </svg>
  <h2 class="panel-title" style="left:248px;top:27px">How we treat?</h2>

  <div class="service" style="left:201px;top:100px"><h3>Manual Therapy</h3><p>Lorem ipsum dolor sit amet, consectetuer adipiscing elit, sed diam nonummy nibh euismod tincidunt ut laoreet dolore magna aliquam erat volutpat. Ut wisi enim ad minim veniam,.</p></div>
  <div class="service" style="left:201px;top:168px"><h3>Manipulation</h3><p>Lorem ipsum dolor sit amet, consectetuer adipiscing elit, sed diam nonummy nibh euismod tincidunt ut laoreet dolore magna aliquam erat volutpat. Ut wisi enim ad minim veniam,.</p></div>
  <div class="service" style="left:201px;top:237px"><h3>Acupuncture</h3><p>Lorem ipsum dolor sit amet, consectetuer adipiscing elit, sed diam nonummy nibh euismod tincidunt ut laoreet dolore magna aliquam erat volutpat. Ut wisi enim ad minim veniam,.</p></div>
  <div class="service" style="left:201px;top:308px"><h3>Exercise</h3><p>Lorem ipsum dolor sit amet, consectetuer adipiscing elit, sed diam nonummy nibh euismod tincidunt ut laoreet dolore magna aliquam erat volutpat. Ut wisi enim ad minim veniam,.</p></div>
  <div class="service" style="left:201px;top:377px"><h3>Craniosacral Therapy</h3><p>Lorem ipsum dolor sit amet, consectetuer adipiscing elit, sed diam nonummy nibh euismod tincidunt ut laoreet dolore magna aliquam erat volutpat. Ut wisi enim ad minim veniam,.</p></div>

  <div class="service" style="left:396px;top:24px"><h3>Custom Foot Orthotics</h3><p>Lorem ipsum dolor sit amet, consectetuer adipiscing elit, sed diam nonummy nibh euismod tincidunt ut laoreet dolore magna aliquam erat volutpat. Ut wisi enim ad minim veniam,.</p></div>
  <div class="service" style="left:396px;top:91px"><h3>Fitness Facilities</h3><p>Lorem ipsum dolor sit amet, consectetuer adipiscing elit, sed diam nonummy nibh euismod tincidunt ut laoreet dolore magna aliquam erat volutpat. Ut wisi enim ad minim veniam,.</p></div>
  <div class="service" style="left:396px;top:160px"><h3>Massage Therapy</h3><p>Lorem ipsum dolor sit amet, consectetuer adipiscing elit, sed diam nonummy nibh euismod tincidunt ut laoreet dolore magna aliquam erat volutpat. Ut wisi enim ad minim veniam,.</p></div>
  <div class="service" style="left:396px;top:229px"><h3>Motor Vehicle Accident</h3><p>Lorem ipsum dolor sit amet, consectetuer adipiscing elit, sed diam nonummy nibh euismod tincidunt ut laoreet dolore magna aliquam erat volutpat. Ut wisi enim ad minim veniam,.</p></div>
  <div class="service" style="left:396px;top:302px"><h3>Pilates</h3><p>Lorem ipsum dolor sit amet, consectetuer adipiscing elit, sed diam nonummy nibh euismod tincidunt ut laoreet dolore magna aliquam erat volutpat. Ut wisi enim ad minim veniam,.</p></div>
  <div class="service" style="left:396px;top:372px"><h3>Running Assessments</h3><p>Lorem ipsum dolor sit amet, consectetuer adipiscing elit, sed diam nonummy nibh euismod tincidunt ut laoreet dolore magna aliquam erat volutpat. Ut wisi enim ad minim veniam,.</p></div>
</section>

</body>
</html>
```